Hydroponic Farm Needs a Business Card

We need a business card design for a hydroponic farm located on the Gulf Coast called 'Tallowbend Farms'. We grow many forms of lettuce and tomatoes along with other herbs and spices. We currently sell to farmer's markets though will soon be expanding to commercial accounts such as restaurants and grocery stores. The colors should be bright and vibrant to reflect the nature of our produce. The final design should communicate a professional, clean, yet friendly impression and able to be used both with farmer's markets and commercial accounts.

The pictures are an example of our product. The pictures do not have to be incorporated into the business card design.

Please put areas for information such as Names, Phone Number, E-mail address, and additional information.

Industry/Entity Type

Farm

```html
<!DOCTYPE html>
<html lang="en">
<head>
<meta charset="utf-8">
<title>Tallowbend Farms – Business Card</title>
<link rel="stylesheet" href="https://fonts.googleapis.com/css2?family=Oswald:wght@600&family=Bebas+Neue&family=Abel&family=Arimo&display=swap">
<style>
  :root {
    --produce-dark: #3a2c1c;
    --produce-red: #b92f28;
    --produce-green: #6a7a38;
    --rule-grey: #5b4f4b;
    --maroon: #5c1b2c;
    --maroon-deep: #4a1a2c;
    --lime: #a3c936;
    --logo-grey: #9b9ca1;
    --white: #ffffff;
    --ink: #3a2a22;
    --rule-dark: #3b2a24;
  }
  * { margin: 0; padding: 0; box-sizing: border-box; }
  html, body { width: 1050px; height: 1200px; overflow: hidden; }
  body { background: var(--lime); }
  .card { position: relative; width: 1050px; height: 1200px; overflow: hidden; background: var(--lime); }

  .produce-photo {
    position: absolute; left: 0; top: 0; width: 1050px; height: 393px;
    background:
      radial-gradient(ellipse 420px 240px at 720px 260px, var(--produce-red) 0%, rgba(185,47,40,0.6) 55%, rgba(185,47,40,0) 100%),
      radial-gradient(ellipse 220px 160px at 260px 220px, rgba(185,47,40,0.75) 0%, rgba(185,47,40,0) 100%),
      linear-gradient(90deg, var(--produce-green) 0%, var(--produce-dark) 35%, var(--produce-dark) 75%, var(--produce-green) 100%);
  }
  .photo-rule { position: absolute; left: 0; top: 393px; width: 1050px; height: 6px; background: var(--rule-grey); }

  .brand-band { position: absolute; left: 0; top: 399px; width: 1050px; height: 201px; background: var(--maroon); }

  .brand-name {
    position: absolute; font-family: "Oswald", "Arial Narrow", sans-serif; font-weight: 600;
    text-transform: uppercase; line-height: 1; white-space: nowrap;
  }
  .brand-tagline {
    position: absolute; font-family: "Arimo", Arial, sans-serif; text-transform: uppercase;
    line-height: 1; white-space: nowrap; color: var(--white); display: flex; align-items: center;
  }
  .brand-tagline .dot { display: inline-block; border-radius: 50%; background: var(--white); }

  .band-name { left: 128px; top: 428px; font-size: 64px; letter-spacing: 1px; color: var(--logo-grey); }
  .band-tagline { left: 186px; top: 500px; font-size: 34px; letter-spacing: 1px; }
  .band-tagline .dot { width: 30px; height: 30px; margin-right: 24px; background: #2d8f3c; }

  .card-name { right: 78px; top: 648px; font-size: 42px; color: var(--maroon-deep); }
  .card-tagline { right: 78px; top: 698px; font-size: 28px; letter-spacing: 1px; }
  .card-tagline .dot { width: 22px; height: 22px; margin-right: 26px; background: #2d8f3c; }
  .card-rule { position: absolute; left: 540px; top: 750px; width: 432px; height: 2px; background: var(--rule-dark); }

  .person-name {
    position: absolute; left: 75px; top: 834px; font-family: "Bebas Neue", "Oswald", sans-serif;
    font-size: 46px; line-height: 1; color: var(--white); letter-spacing: 1px;
  }
  .person-role {
    position: absolute; left: 133px; top: 877px; font-family: "Bebas Neue", "Oswald", sans-serif;
    font-size: 30px; line-height: 1; color: var(--ink);
  }
  .contact {
    position: absolute; font-family: "Abel", "Arial Narrow", sans-serif; font-size: 23px;
    line-height: 35px; color: var(--ink); letter-spacing: 1px; white-space: nowrap;
  }
  .contact-phone { left: 75px; top: 968px; }
  .contact-email { left: 75px; top: 1046px; }
  .contact-web { left: 540px; top: 1046px; }
</style>
</head>
<body>
<main class="card">
  <div class="produce-photo" role="img" aria-label="Posterized photograph of ripe red tomatoes on the vine among green leaves"></div>
  <div class="photo-rule"></div>

  <section class="brand-band">
  </section>
  <div class="brand-name band-name">Tallowbend Farms</div>
  <div class="brand-tagline band-tagline"><span class="dot"></span>Hydrophonics</div>

  <div class="brand-name card-name">Tallowbend Farms</div>
  <div class="brand-tagline card-tagline"><span class="dot"></span>Hydrophonics</div>
  <div class="card-rule"></div>

  <div class="person-name">Lorem Ipsum</div>
  <div class="person-role">Incogniti</div>

  <div class="contact contact-phone">091.555.0142</div>
  <div class="contact contact-email">loremipsum@tallowbendfarms.com</div>
  <div class="contact contact-web">http://www.tallowbendfarms.com<br>Twitter: @tallowbendfarms</div>
</main>
</body>
</html>
```